Beer labels for craft beer brewery

For a newly founded micro-brewery in Eastern Austria, we need beer labels to start production. We will be starting with three beer-variations, thus different 4 labels total (Basic label + 3 variations). The beers are made of natural ingredients (water, hop&malt) sourced locally and we are aiming to attain bio-certification. The motto is "Aus Quelle ins Krüglein" (From the spring to the mug) and expresses the natural, circular and honest way of brewing beer. The Brewery's name is "Falkenhoff" (Falkenhoff-brewery), as in the history of the village, where the brewery is located, the former "head farmer" was nicknamend "Falke", as he talked like a politician and liked to inform his fellow citizens in the ways of the world...
Updates

Dear Designers, Customer has now uploaded their logo design for their business. Please use this and resubmit a label design using the Logo. Regards, DC Admin Bartholomew

Target Market(s)

regional Beer aficionados, local pub & restaurant patrons who value naturally manufactured premium craft beer.

Logo Text

Falkenhoff - aus Quelle ins Krüglein (logo already designed)

Requirements
Must have
• Basic label and variations with color patterns and black&white version, end product: 4 recognizable individual beer labels as briefed.
Lable design & coloring must fit to brown color of beer bottles (no cans).
Nice to have
• Iconic label that is recognizeable and leaves a first impression...and "thirst" impression....
Should not have
• Beer can labels.

```html
<!DOCTYPE html>
<html lang="de">
<head>
<meta charset="utf-8">
<title>Falkenhoff – Klare Quelle Label</title>
<link rel="stylesheet" href="https://fonts.googleapis.com/css2?family=Oswald:wght@500;600&display=swap">
<style>
  :root {
    --backdrop: #2b2a2a;
    --label-black: #0d0d0d;
    --gold-light: #f3d98a;
    --gold-mid: #c9a04a;
    --gold-dark: #8a6422;
    --ink: #141414;
  }
  html, body {
    margin: 0;
    padding: 0;
    width: 849px;
    height: 1200px;
    overflow: hidden;
    background: var(--backdrop);
  }
  .label-canvas {
    display: block;
    width: 849px;
    height: 1200px;
  }
  .brand-name {
    font-family: "Oswald", sans-serif;
    font-weight: 600;
    font-size: 84px;
    letter-spacing: 4px;
    fill: var(--ink);
  }
  .beer-variety {
    font-family: "Oswald", sans-serif;
    font-weight: 500;
    font-size: 30px;
    letter-spacing: 6px;
    fill: var(--gold-mid);
  }
  .quality-mark {
    font-family: "Oswald", sans-serif;
    font-weight: 500;
    font-size: 24px;
    letter-spacing: 4px;
    fill: var(--gold-mid);
  }
</style>
</head>
<body>
<svg class="label-canvas" viewBox="0 0 849 1200" xmlns="http://www.w3.org/2000/svg">
  <defs>
    <linearGradient id="gold-sheen" x1="0" y1="0" x2="1" y2="1">
      <stop offset="0" stop-color="var(--gold-dark)"/>
      <stop offset="0.35" stop-color="var(--gold-light)"/>
      <stop offset="0.6" stop-color="var(--gold-mid)"/>
      <stop offset="1" stop-color="var(--gold-dark)"/>
    </linearGradient>
    <linearGradient id="gold-band" x1="0" y1="0" x2="0" y2="1">
      <stop offset="0" stop-color="var(--gold-light)"/>
      <stop offset="0.5" stop-color="var(--gold-mid)"/>
      <stop offset="1" stop-color="var(--gold-dark)"/>
    </linearGradient>
  </defs>

  <rect class="backdrop" width="849" height="1200" fill="var(--backdrop)"/>

  <g class="label">
    <ellipse class="label-outer-rim" cx="424.5" cy="600" rx="255" ry="370" fill="var(--label-black)" stroke="url(#gold-sheen)" stroke-width="12"/>
    <ellipse class="label-inner-rim" cx="424.5" cy="600" rx="232" ry="346" fill="none" stroke="url(#gold-sheen)" stroke-width="3"/>

    <g class="mascot-emblem" role="img" aria-label="Gold illustration of the brewery's orator figure">
      <ellipse cx="424.5" cy="420" rx="78" ry="100" fill="url(#gold-sheen)" opacity="0.9"/>
    </g>

    <g class="name-banner">
      <rect x="140" y="548" width="569" height="112" fill="url(#gold-band)"/>
      <rect x="150" y="556" width="549" height="96" fill="none" stroke="var(--ink)" stroke-width="2"/>
      <text class="brand-name" x="424.5" y="636" text-anchor="middle">FALKENHOFF</text>
    </g>

    <line class="rule" x1="280" y1="694" x2="569" y2="694" stroke="var(--gold-mid)" stroke-width="2"/>
    <text class="beer-variety" x="424.5" y="734" text-anchor="middle">KLARE QUELLE</text>
    <line class="rule" x1="280" y1="752" x2="569" y2="752" stroke="var(--gold-mid)" stroke-width="2"/>

    <rect class="quality-frame" x="322" y="786" width="205" height="42" fill="none" stroke="var(--gold-mid)" stroke-width="2"/>
    <text class="quality-mark" x="424.5" y="816" text-anchor="middle">BEST QUALITY</text>
  </g>
</svg>
</body>
</html>
```